Brand refresh of quote, work docket and Fire certificate documents

I would like a refresh of our document suit including

1. Front page called VANTO3 Proposal
2. Quote document template
3. Work docket template
4. Fire certificate template - to look like a professional complaint certificate

Examples of documents are attached.

```html
<!DOCTYPE html>
<html lang="en">
<head>
<meta charset="utf-8">
<title>VANTO3 Work Docket 1188</title>
<link rel="stylesheet" href="https://fonts.googleapis.com/css2?family=Source+Sans+3:wght@400;600;700;800&display=swap">
<style>
:root{
  --page-bg:#dcdcde;
  --sheet:#f4f4f6;
  --ink:#222226;
  --logo-grey:#3b3b3f;
  --orange:#f28a26;
  --orange-light:#f6a531;
  --red:#e23b3f;
  --red-deep:#e63c37;
  --row-pink:#f3c5c8;
  --row-peach:#fcd9a8;
  --photo-a:#9a9a98;
  --photo-b:#c9c8c4;
}
*{margin:0;padding:0;box-sizing:border-box}
html,body{width:1200px;height:2182px;overflow:hidden}
body{background:var(--page-bg);font-family:"Source Sans 3",sans-serif;color:var(--ink);position:relative}
.docket{position:absolute;left:50px;top:314px;width:956px;height:1350px;background:var(--sheet);transform:scale(1.1506);transform-origin:top left;overflow:hidden;box-shadow:0 6px 18px rgba(0,0,0,.25)}
.brand{position:absolute;left:62px;top:40px}
.brand-row{display:flex;align-items:center;gap:10px}
.brand-mark{width:22px;height:22px;background:var(--red);border-radius:50%}
.brand-name{font-weight:800;font-size:96px;line-height:1;color:var(--logo-grey);letter-spacing:-2px}
.brand-tag{margin-top:8px;font-size:15px;letter-spacing:5.2px;color:var(--logo-grey)}
.site-photo{position:absolute;left:524px;top:0;width:432px;height:528px;border-top-left-radius:80px;background:linear-gradient(160deg,var(--photo-b),var(--photo-a))}
.address-panel{position:absolute;left:0;top:190px;width:606px;height:338px;border-top-right-radius:80px;background:linear-gradient(20deg,var(--red-deep) 0%,var(--orange) 45%,var(--orange-light) 100%);color:#fff;padding:20px 0 0 47px}
.date{font-size:17px}
.to{margin-top:18px;font-weight:700;font-size:17px}
.client{font-weight:700;font-size:26px;line-height:1.1}
.client-address{margin-top:12px;font-weight:700;font-size:18px;line-height:21px}
.docket-no{margin-top:20px;font-weight:700;font-size:18px}
.site-note{margin-top:18px;font-size:18px;line-height:21px}
.tab{position:absolute;left:0;height:40px;padding:0 26px 0 28px;border-radius:0 20px 20px 0;background:linear-gradient(90deg,var(--red-deep),var(--orange) 60%,var(--orange-light));color:#fff;font-weight:700;font-size:29px;line-height:40px}
.tab-small{height:38px;font-size:23px;line-height:38px}
.works{position:absolute;top:612px;width:420px}
.works.left{left:28px}.works.right{left:467px;width:470px}
.area{margin-bottom:17px}
.area h3{font-weight:700;font-size:20px;line-height:24px;color:var(--red)}
.area h3 span{color:var(--orange)}
.area p{font-size:15.5px;line-height:17.5px;margin-top:3px}
.area p+p{margin-top:8px}
.labour{position:absolute;left:28px;top:1101px;font-size:15.5px}
.breakdown{position:absolute;left:28px;top:1228px;font-size:15.5px;font-weight:600;line-height:25.8px}
.materials{position:absolute;left:491px;top:1052px;width:371px;border-collapse:collapse;font-size:15px}
.materials th{background:var(--orange);color:#fff;text-align:left;font-weight:700;font-size:23px;height:27px;padding:0 12px;line-height:27px}
.materials td{height:24px;padding:0 12px}
.materials tr:nth-child(odd) td{background:var(--row-pink)}
.materials tr:nth-child(even) td{background:var(--row-peach)}
.materials td.price{width:120px}
.footer{position:absolute;left:443px;top:1233px;width:513px;height:117px;border-top-left-radius:30px;background:linear-gradient(90deg,var(--orange) 0%,var(--red-deep) 100%);color:#fff;padding:10px 0 0 14px}
.footer h4{font-weight:700;font-size:20px}
.footer p{font-size:16px;line-height:26px;font-weight:600}
.base-strip{position:absolute;left:0;bottom:0;width:956px;height:10px;background:linear-gradient(90deg,var(--red-deep),var(--orange))}
</style>
</head>
<body>
<main class="docket">
  <div class="brand">
    <div class="brand-row"><span class="brand-mark"></span><span class="brand-name">VANTO3</span></div>
    <div class="brand-tag">PASSIVE FIRE PROTECTION</div>
  </div>
  <div class="site-photo" role="img" aria-label="Photo from above of two workers in blue hard hats and yellow vests reviewing tablets on a concrete floor"></div>
  <section class="address-panel">
    <div class="date">26th October, 2023</div>
    <div class="to">TO</div>
    <div class="client">MARLOW BUILDERS</div>
    <div class="client-address">48 Harbour St<br>Westbank VIC 3207<br>Stefano</div>
    <div class="docket-no">Work Docket: 1188</div>
    <div class="site-note">Works completed at 14 Ardent Street, Kelsey Park as directed<br>by Stefano of Marlow Builders as listed below.</div>
  </section>

  <div class="tab" style="top:558px">WORKS COMPLETED:</div>
  <section class="works left">
    <div class="area"><h3>BASEMENT 1 – <span>FAN ROOM</span></h3><p>1 x 20mm x 20mm penetration with conduit through<br>blockwork wall (?)</p></div>
    <div class="area"><h3>BASEMENT 1 – <span>APARTMENT 38 GARAGE</span></h3><p>2 x 100mm x 100mm penetration with sprinkler pipe &amp; wrap<br>through slab wall (Wet Fire)</p></div>
    <div class="area"><h3>BASEMENT 1 – <span>APARTMENT 34 GARAGE</span></h3><p>2 x 100mm x 100mm penetration with sprinkler pipe &amp; wrap<br>through slab wall (Wet Fire)</p></div>
    <div class="area"><h3>BASEMENT 1 – <span>APARTMENT 30 GARAGE</span></h3><p>2 x 100mm x 100mm penetration with sprinkler pipe &amp; wrap<br>through slab wall (Wet Fire)</p></div>
    <div class="area"><h3>BASEMENT 1 – <span>APARTMENT 28</span></h3><p>5mtrs of caulking through slab wall (one side only) (Brickies)</p></div>
  </section>
  <section class="works right">
    <div class="area"><h3>BASEMENT 1 – <span>BACK STAIRWELL</span></h3><p>1 x 400mm x 400mm penetration empty through blockwork wall<br>(Builder)</p></div>
    <div class="area"><h3>BASEMENT 1 – <span>APARTMENT BIN ROOM</span></h3><p>1 x 80mm x 80mm penetration with sprinkler pipe &amp; wrap through<br>blockwork wall (Wet Fire)</p><p>2 x 20mm x 20mm penetration with conduit through blockwork wall (?)<br>2 x 20mm x 20mm penetration with conduit through blockwork wall (?)</p></div>
    <div class="area"><h3>BASEMENT 1 – <span>COMMS ROOM</span></h3><p>2 x 300mm x 300mm penetration empty through slab wall (Builder)</p></div>
    <div class="area"><h3>BASEMENT 1 – <span>SWITCHBOARD ROOM</span></h3><p>1 x 400mm x 100mm penetration empty through blockwork wall<br>(Builder)</p><p>12mtrs of caulking through blockwork wall (one side only) (Brickies)</p></div>
  </section>

  <div class="tab tab-small" style="top:1052px">LABOUR</div>
  <p class="labour">21/10/23&nbsp; 2 Men x 5hrs = 10hrs&nbsp;&nbsp;&nbsp; $1500.00 (time &amp; a half rate)</p>

  <div class="tab tab-small" style="top:1178px">BREAKDOWN:</div>
  <div class="breakdown">
    <p>Conduits (unknown) 10% - 291.50 + GST</p>
    <p>Wet Fire 45% - $1,311 + GST</p>
    <p>Brickies 20% - $583 + GST</p>
    <p>Builder 25% - $728.75 + GST</p>
  </div>

  <table class="materials">
    <thead><tr><th colspan="2">MATERIALS</th></tr></thead>
    <tbody>
      <tr><td>1 x Fire Mortar (20kg bag)</td><td class="price">$150.00</td></tr>
      <tr><td>2 x Rod (Bundle)</td><td class="price">$100.00</td></tr>
      <tr><td>15 x Caulk (Ltr)</td><td class="price">$375.00</td></tr>
      <tr><td>4 x HPE 300ml</td><td class="price">$120.00</td></tr>
      <tr><td>1 x Sealwrap 40 (Roll)</td><td class="price">$220.00</td></tr>
      <tr><td>¾ x Flexiwrap (Roll)</td><td class="price">$450.00</td></tr>
    </tbody>
  </table>

  <div class="base-strip"></div>
  <footer class="footer">
    <h4>VANTO3 PTY LTD</h4>
    <p>3/22 Ridgeway Street Oakleigh VIC 3166</p>
    <p>ABN: 98 765 432 109 | admin@vanto3.com.au | www.vanto3.com.au</p>
  </footer>
</main>
</body>
</html>
```